Psychotherapy Website - Based in London

I am a newly trained psychotherapist and need a new website for www.delphinecarrow.co.uk.

I offer therapy for addiction, relationships, trauma and many other issues people face in their lives.

I want the website to be welcoming, gentle, feminine and for people to feel safe.

I do not like a page site that scrolls through sections, rather each page should be separate. Here some examples that i like. Sectional rather than scrolled.

https://www.maribethvane.com/
https://www.thequietrooms.com/

The imagery should be around pink using the flower in the logo / wording and around the site:

Here is a link to the flower for ideas:
https://www.lookfindo.com/search?q=pink+gerbera

DelphineCarrow
Compassionate Psychotherapy

Is the logo and subheader for the website. Please use a typeface for the name that is appealing and professional.

Type face similar NOT EXLUSIVLY - JUST AN IDEA like this:
https://glowpostureclub.com/

Basic business card i created as a rough idea below.

I have also added the website copy.

The headers are

Homepage
About Me
Therapy
Common Questions
Blog
Contact Me

Target Market(s)

Clients who are dealing with stress, trauma, pain, addiction

Industry/Entity Type

Therapy and Psychology

Coding

Coded - Design and coding required

Number of Pages Required

5+ page

Font styles to use
Serif
Sans Serif
Script

Colors
0054AA
0677BA
7BADD7
CADEEF
E8F1F8
0094D4
00A9DD
6FCCEA
C7EBF8
E9F6FB
E54698
E96AAD
F1A4CE
F9D9EA
FCEFF6

Requirements
Must have
• Pink Gerbera Flower integrated into design
Nice to have
• Images but not to stock imagery. Needs to look authentic and natural
Should not have
• Stock images of people. Images are important but needs to feel REAL

```html
<!DOCTYPE html>
<html lang="en">
<head>
<meta charset="utf-8">
<title>DelphineCarrow – Compassionate Psychotherapy</title>
<link rel="stylesheet" href="https://fonts.googleapis.com/css2?family=Playfair+Display:wght@400;700&family=Poppins:wght@400;500;600&display=swap">
<style>
:root{
  --navy:#0054AA;
  --mid-blue:#0677BA;
  --sky:#0094D4;
  --bright:#00A9DD;
  --soft-blue:#6FCCEA;
  --pale-blue:#E9F6FB;
  --pink:#E54698;
  --pink-mid:#E96AAD;
  --pink-soft:#F1A4CE;
  --pink-pale:#F9D9EA;
  --pink-mist:#FCEFF6;
  --petal:#f4b3aa;
  --ink:#2a2a2a;
  --body:#4a4a4a;
  --muted:#8a8a8a;
  --canvas:#eef1f5;
  --serif:'Playfair Display', Georgia, serif;
  --sans:'Poppins', Arial, sans-serif;
}
*{margin:0;padding:0;box-sizing:border-box}
html,body{width:1200px;height:4980px;overflow:hidden}
body{background:var(--canvas);font-family:var(--sans);color:var(--body)}
.page{position:absolute;left:106px;top:70px;width:966px;height:4808px;background:#fff;overflow:hidden}
.abs{position:absolute}
.accent{color:var(--navy)}
.pink{color:var(--pink)}

/* hero */
.hero{left:0;top:0;width:966px;height:496px;background:linear-gradient(180deg,#a9d8e4 0%,#8fcbe0 55%,#6fb6d9 100%)}
.brand{left:0;top:34px;width:966px;text-align:center;font-family:var(--serif);color:#2f74c0;font-size:31px;line-height:43px}
.nav{left:0;top:496px;width:966px;height:58px;background:var(--sky);display:flex;justify-content:center;align-items:center;gap:50px}
.nav a{color:#fff;font-size:12px;text-decoration:none}

/* intro */
.intro{left:0;top:554px;width:966px;height:520px;background:linear-gradient(90deg,var(--pink-mist) 0%,#f6f6f8 30%,#f6f6f8 70%,var(--pink-mist) 100%)}
.intro h1{position:absolute;left:0;top:52px;width:966px;text-align:center;font-family:var(--serif);font-weight:400;font-size:21px;line-height:27px;color:var(--ink);text-transform:uppercase}
.intro .copy{position:absolute;left:143px;top:120px;width:680px;text-align:center;font-size:11px;line-height:18px}
.intro .copy p{margin-bottom:18px}
.divider{left:415px;top:455px;width:136px;height:12px}

/* trainee */
.trainee{left:0;top:1074px;width:966px;height:380px;background:#f1f1f4}
.portrait{left:104px;top:40px;width:283px;height:292px;background:linear-gradient(160deg,#e8e4df,#d9c7b8 60%,#e06a8f 100%);border-right:3px solid var(--pink)}
.trainee h2{position:absolute;left:481px;top:50px;font-family:var(--serif);font-weight:400;font-size:21px;color:var(--ink)}
.trainee .copy{position:absolute;left:481px;top:98px;width:370px;font-size:11px;line-height:18px}
.trainee .copy p{margin-bottom:18px}

/* therapy */
.therapy{left:0;top:1454px;width:966px;height:486px;background:#f1f1f4}
.flower-big{left:540px;top:-60px;width:426px;height:546px;background:linear-gradient(120deg,rgba(241,241,244,0) 0%,rgba(249,217,210,.7) 25%,var(--petal) 55%,#f6c4bb 80%,rgba(241,241,244,0) 100%)}
.therapy h2{position:absolute;left:93px;top:22px;font-family:var(--serif);font-weight:400;font-size:24px;line-height:32px;color:var(--ink);text-transform:uppercase}
.therapy .copy{position:absolute;left:93px;top:104px;width:440px;font-size:11px;line-height:16px}
.therapy .copy p{margin-bottom:16px}
.btn{display:inline-block;background:var(--sky);color:#fff;font-size:11px;padding:11px 14px}
.therapy .btn{position:absolute;left:100px;top:410px}

/* help */
.help{left:0;top:1940px;width:966px;height:550px;background:linear-gradient(180deg,#2aa7dc 0%,#1b8fd0 60%,#2b9ad6 100%)}
.help h2{position:absolute;left:0;top:100px;width:966px;text-align:center;font-family:var(--serif);font-weight:400;font-size:24px;color:#fff}
.topics{position:absolute;left:70px;top:158px;width:827px;display:grid;grid-template-columns:repeat(3,251px);column-gap:37px;row-gap:10px}
.topics span{height:36px;border:1.5px solid #fff;color:#fff;font-size:15px;display:flex;align-items:center;justify-content:center}
.arrows{left:453px;top:462px;width:60px;height:20px}

/* questions */
.faq{left:0;top:2490px;width:966px;height:448px;background:#f7f7f7}
.thinker{left:106px;top:87px;width:261px;height:361px;background:linear-gradient(180deg,#f7f7f7 0%,#d9cfc6 30%,#a9c4dd 70%,#89aed3 100%)}
.faq h2{position:absolute;left:425px;top:76px;font-family:var(--serif);font-weight:700;font-size:21px;color:var(--ink)}
.q{position:absolute;left:429px;width:430px;font-size:17px;font-weight:600;letter-spacing:.4px}
.q.open{top:114px;color:var(--navy)}
.q.one{top:344px;color:var(--pink)}
.q.two{top:376px;color:var(--pink)}
.q i{position:absolute;right:0;top:0;font-style:normal;font-weight:300;font-size:26px;line-height:22px;color:var(--ink)}
.q.open i{color:var(--navy)}
.answer{position:absolute;left:455px;top:160px;width:390px;font-size:11px;line-height:17px}

/* blog */
.blog{left:0;top:2938px;width:966px;height:537px;background:#ececec}
.blog h2{position:absolute;left:0;top:58px;width:966px;text-align:center;font-family:var(--serif);font-weight:400;font-size:34px;color:var(--ink);text-transform:uppercase}
.card{position:absolute;top:184px;width:203px;height:290px;background:#fff}
.card .thumb{height:112px}
.card .meta{margin:12px 12px 0;font-size:8px;color:#666}
.card h3{margin:6px 12px 0;font-size:12px;font-weight:400;line-height:17px;color:var(--ink)}
.card .excerpt{margin:8px 12px 0;font-size:7px;line-height:10px;color:#aaa}
.card a{display:block;margin:6px 12px 0;font-size:9px;color:var(--sky)}

/* feature */
.feature{left:0;top:3475px;width:966px;height:535px;background:linear-gradient(90deg,var(--pink-pale) 0%,#fff 35%,#fff 65%,var(--pink-mist) 100%)}
.feature-photo{left:155px;top:81px;width:371px;height:374px;background:linear-gradient(160deg,#4d5566 0%,#7a7f8c 45%,#c4a184 100%)}
.feature-card{left:452px;top:101px;width:389px;height:382px;background:#fff;box-shadow:0 6px 24px rgba(0,0,0,.12);padding:30px 32px}
.feature-card h2{font-family:var(--serif);font-weight:700;font-size:22px;line-height:32px;color:var(--ink);text-transform:uppercase}
.feature-card p{margin-top:18px;font-size:11px;line-height:17px}
.feature-card .btn{margin-top:18px;font-size:9px;padding:7px 20px;font-weight:600}

/* contact */
.contact{left:0;top:4010px;width:966px;height:460px}
.contact h2{position:absolute;left:62px;top:92px;font-family:var(--serif);font-weight:700;font-size:30px;color:var(--ink)}
.block{position:absolute;font-size:11px;line-height:18px;color:var(--ink)}
.block h3{font-size:20px;font-weight:500;margin-bottom:10px;text-transform:uppercase}
.row{display:flex;gap:14px;align-items:flex-start}
.map{left:628px;top:84px;width:269px;height:270px;background:linear-gradient(135deg,#e6efe1 0%,#d7e9f1 50%,#e9ecde 100%);border:1px solid #ddd}
.dots{display:flex;gap:18px}
.dots b{width:10px;height:10px;border-radius:50%;background:var(--ink);display:block}

/* footer */
.footer{left:0;top:4470px;width:966px;height:338px;background:var(--sky);color:#fff}
.footer-flower{left:438px;top:4420px;width:90px;height:90px;border-radius:50%;background:linear-gradient(135deg,var(--pink-soft),var(--pink-mid))}
.fcol{position:absolute;top:110px;font-size:10px;line-height:21px}
.fcol h4{font-size:15px;font-weight:500;margin-bottom:8px}
.fcol ul{list-style:none}
.fcol li::before{content:"•";margin-right:14px}
.subscribe{position:absolute;left:619px;top:200px;width:272px;height:40px;background:#fff;border-radius:20px;font-size:9px;color:#555;padding:14px 18px}
.subscribe span{position:absolute;right:0;top:0;width:98px;height:40px;border-radius:20px;background:var(--navy);color:#fff;display:flex;align-items:center;justify-content:center}
.rule{position:absolute;left:74px;top:262px;width:818px;height:1px;background:rgba(255,255,255,.5)}
.copyright{position:absolute;left:0;top:282px;width:966px;text-align:center;font-size:10px}
.social{position:absolute;left:412px;top:306px;display:flex;gap:24px}
.social b{width:12px;height:12px;border-radius:50%;background:#fff;display:block}
</style>
</head>
<body>
<div class="page">

  <div class="abs hero" role="img" aria-label="Open hand beneath a sad face and a smiling face on a soft blue background"></div>
  <div class="abs brand">DelphineCarrow<br>Compassionate Psychotherapy</div>
  <nav class="abs nav">
    <a href="#">Home</a><a href="#">About Me</a><a href="#">Therapy</a><a href="#">Common Questions</a><a href="#">Blog</a><a href="#">Contact Me</a>
  </nav>

  <section class="abs intro">
    <h1>Taking The First Steps Towards Engaging In<br><span class="accent">Therapy</span> Can Be A Very Personal Journey.</h1>
    <div class="copy">
      <p>Whilst, It Can Be Challenging, I Will Ensure To Make This Journey As Safe And As Comfortable For You As Possible.</p>
      <p>Psychotherapy Can Help You See Your Current Situation In New Light, Depth And Clarity. It Can Change Old And Unhelpful Perspectives And Feelings About Yourself And Your Life, And Ultimately Help You Make Positive Changes. It Might Be The Most Important Journey You'll Ever Make.</p>
      <p>I Provide A And Non-Judgmental Space Where Any Issues Can Be Explored In Complete Confidentiality.</p>
      <p>My Practice Is Based In Richmond, Where The Room Is Homely, Comfortable And Welcoming. I Believe A Good Environment Contributes To Great Therapy.</p>
      <p>Alternatively, I Am Also Available To Provide Therapy Online, If This Environment Is More Accommodating For My Clients.</p>
      <p>I Am Passionate About Improving Mental Health And Committed To Offering Therapy To All Individuals Regardless Of Their Age, Race, Culture, Disability, Sexual Orientation, Or Socio-Economic Background.</p>
    </div>
    <svg class="abs divider" viewBox="0 0 136 12" aria-hidden="true"><line x1="0" y1="6" x2="56" y2="6" stroke="#555" stroke-width="1.5"/><line x1="80" y1="6" x2="136" y2="6" stroke="#555" stroke-width="1.5"/></svg>
  </section>

  <section class="abs trainee">
    <div class="abs portrait" role="img" aria-label="Portrait photograph of the therapist"></div>
    <h2>TRAINEE <span class="accent">PHYSIOTHERAPIST</span></h2>
    <div class="copy">
      <p>I Have Over 10 Years' Experience Of Dealing With Addictions. Addictions Are Often More Of A Solution To Fear And Emotional Pain. However, Eventually The Addiction Causes More Problems. I Know Recovery Is Possible With The Right Support.</p>
      <p>I Have Also Had Some Twenty Years Of Experience Of Dealing With Mental Health Issues Such As Depression, Anxiety, Complex PTSD And Trauma. It Is Possible To Manage These Issues And Live A Full Life.</p>
      <p>I Have Worked In The Voluntary Sector As A Helpline Listener And Am Currently A Therapist For Kindred Minds.</p>
    </div>
  </section>

  <section class="abs therapy">
    <div class="abs flower-big" role="img" aria-label="Photograph of a large pink gerbera flower"></div>
    <h2><span class="accent">Therapy</span> With<br>DelphineCarrow</h2>
    <div class="copy">
      <p>There are times when the challenges of life can make us feel overwhelmed and isolated, and it may feel difficult to talk about how we feel to those who are closest to us. We go through transitions and crises and experience uncertainty and loss. How we deal with difficulties in life is an important aspect in how we carry on forwards and ultimately who we become as people.</p>
      <p>I offer a range of psychotherapeutic approaches including transactional analysis psychotherapy and relational therapy.</p>
      <p>Through the process of exploration, we enable self-knowledge and self-awareness to help you grow and conquer issues that may previously have been experienced as all-consuming or overwhelming. We will not only look at your problems in the present but also identify the roots of these problems from your past. We will explore how your past experiences may have affected the way you live today and operate within your life in the present and when you become aware and understand this, it is possible for change to take place.</p>
    </div>
    <span class="btn">About Therapy</span>
  </section>

  <section class="abs help" role="img" aria-label="Blue-tinted photograph of a therapy conversation">
    <h2>WHAT WE CAN HELP WITH</h2>
    <div class="topics">
      <span>Addiction</span><span>Anger</span><span>Anxiety</span>
      <span>Bullying</span><span>Career Changes</span><span>Crisis/Breakdown</span>
      <span>Depression</span><span>Difficulty making desission</span><span>Emotional abuse</span>
      <span>Fear</span><span>Feeling alone/isolated</span><span>Health Issues</span>
      <span>HIV</span><span>Identity Issues</span><span>Lowe self confidence</span>
      <span>Loss of meaning</span><span>LGBT issues</span><span>Negative thinking</span>
    </div>
    <svg class="abs arrows" viewBox="0 0 60 20" aria-hidden="true" fill="none" stroke="#fff" stroke-width="1.5"><path d="M24 10H4M10 4L4 10l6 6"/><path d="M36 10h20M50 4l6 6-6 6"/></svg>
  </section>

  <section class="abs faq">
    <div class="abs thinker" role="img" aria-label="Photograph of a thoughtful man in a blue shirt"></div>
    <h2>COMMON QUESTIONS</h2>
    <div class="q open">HOW LONG WILL I NEED THERAPY FOR?<i>—</i></div>
    <p class="answer">Therapy can last anywhere from one session to several months or even years. It all depends on what you want and need. Some people come to therapy with a very specific problem they need to solve and might find that one or two sessions is sufficient. Other people come to therapy with more complicated issues they are grappling with and may feel they need a few months or more to understand and resolve their issues. Other people come with long-standing problems or difficult feelings and may benefit from longer-term therapy.</p>
    <div class="q one">HOW LONG ARE THE SESSIONS?<i>+</i></div>
    <div class="q two">HOW MUCH IS EACH SESSION?<i>+</i></div>
  </section>

  <section class="abs blog">
    <h2>Latest <span class="accent">Blog</span> Posts</h2>
    <article class="card" style="left:130px">
      <div class="thumb" role="img" aria-label="Photograph of a counselling session" style="background:linear-gradient(135deg,#8a7b70,#d9d2cb)"></div>
      <p class="meta">06/02/2021 | <span style="color:var(--sky)">DelphineCarrow</span></p>
      <h3>Three challenges of trauma: why recovery is so hard</h3>
      <p class="excerpt">So we're humans on this planet, every day the same dilemma: we need to go out to find food and shelter, but danger may wait around the corner and we need to stay safe.</p>
      <a href="#">Continue</a>
    </article>
    <article class="card" style="left:367px">
      <div class="thumb" role="img" aria-label="Photograph of a therapist taking notes" style="background:linear-gradient(135deg,#6c6c6c,#c9c4bd)"></div>
      <p class="meta">04/07/2019 | <span style="color:var(--sky)">DelphineCarrow</span></p>
      <h3>Trauma and the bears – a fable</h3>
      <p class="excerpt">Once upon a time, there were humans on the savannah. It was a dangerous world. We needed to find food, we needed to protect ourselves and we needed shelter.</p>
      <a href="#">Continue</a>
    </article>
    <article class="card" style="left:605px">
      <div class="thumb" role="img" aria-label="Photograph of two people talking on a sofa" style="background:linear-gradient(135deg,#5d5e63,#d8d4cf)"></div>
      <p class="meta">12/09/2020 | <span style="color:var(--sky)">DelphineCarrow</span></p>
      <h3>Why the symptoms of trauma make sense</h3>
      <p class="excerpt">So we're humans on the savannah. We're not bigger or faster than other predators, and we don't have fangs or claws, so our safety lies in numbers and in staying alert.</p>
      <a href="#">Continue</a>
    </article>
  </section>

  <section class="abs feature">
    <div class="abs feature-photo" role="img" aria-label="Photograph of a person resting their head on folded arms"></div>
    <div class="abs feature-card">
      <h2>Why The<br><span class="accent">Symptoms Of Trauma</span><br>Make Sense</h2>
      <p>I looked again at the list of symptoms. It was long, and overwhelming, and ran to more than two pages. 'Signs you've been traumatised' promised the infographic. Many of them were cross-referenced – meticulously, helpfully, well-meaningly – to the diagnostic criteria for PTSD in the psychiatric 'bibles' of mental disorders, the DSM-5 and the ICD-11. This was an impressive, and somewhat intimidating list. More worrying was that I identified with so many of the items on it.</p>
      <span class="btn">LEARN MORE</span>
    </div>
  </section>

  <section class="abs contact">
    <h2>GET IN <span class="accent">TOUCH</span></h2>
    <div class="block" style="left:44px;top:152px">
      <h3>Location</h3>
      <div class="row">
        <svg width="16" height="18" viewBox="0 0 16 18" fill="none" stroke="#222" stroke-width="1.4" aria-hidden="true"><path d="M8 17s6-6 6-10A6 6 0 0 0 2 7c0 4 6 10 6 10z"/><circle cx="8" cy="7" r="2"/></svg>
        <div>Linden Community Centre<br>27 Alder Road East<br>&nbsp;&nbsp;&nbsp;Twickenham&nbsp; TW1 9ZZ</div>
      </div>
    </div>
    <div class="block" style="left:295px;top:148px">
      <h3>Contact Us</h3>
      <div class="row"><svg width="18" height="18" viewBox="0 0 24 24" fill="none" stroke="#222" stroke-width="1.5" aria-hidden="true"><path d="M22 17v3a2 2 0 0 1-2 2A19 19 0 0 1 2 4a2 2 0 0 1 2-2h3l2 5-2.5 1.5a11 11 0 0 0 6 6L14 12l5 2z"/></svg><span>07700 900418</span></div>
      <div class="row" style="margin-top:16px"><svg width="18" height="14" viewBox="0 0 18 14" fill="none" stroke="#222" stroke-width="1.4" aria-hidden="true"><rect x="1" y="1" width="16" height="12"/><path d="M1 1l8 7 8-7"/></svg><span style="text-decoration:underline">hello@delphinecarrow.co.uk</span></div>
    </div>
    <div class="block" style="left:44px;top:291px">
      <h3>Open Hours</h3>
      <div style="padding-left:8px">MON–SAT 09:00 – 09:00<br>SUN :Holiday</div>
    </div>
    <div class="block" style="left:295px;top:291px">
      <h3>Follow Us On</h3>
      <div class="dots" style="padding-left:22px" aria-label="Social links"><b></b><b></b><b></b><b></b></div>
    </div>
    <div class="abs map" role="img" aria-label="Map of the Twickenham area with the practice location marked"></div>
  </section>

  <footer class="abs footer">
    <div class="fcol" style="left:74px"><h4>ABOUT US</h4><ul><li>Our Story</li><li>Our Values</li><li>Our Mission</li><li>Our Blog</li><li>FAQ's</li></ul></div>
    <div class="fcol" style="left:222px"><h4>YOUR JOURNEY</h4><ul><li>Child Sexual Abuse</li><li>Dissociation</li><li>Recovery</li><li>Trauma</li><li>Getting help</li></ul></div>
    <div class="fcol" style="left:404px;font-size:12px"><h4>CONTACT US</h4>
      <div class="row" style="gap:10px"><span>☏</span><span>07700 900418</span></div>
      <div class="row" style="gap:10px;line-height:18px;margin-top:6px"><span>✉</span><span>hello@delphine<br>carrow.co.uk</span></div>
      <div class="row" style="gap:10px;margin-top:6px"><span>⌖</span><span>Get Direction</span></div>
    </div>
    <div class="fcol" style="left:629px;font-size:14px;font-weight:500"><p>Don't Miss Any Opportunity</p><p style="font-size:18px;font-weight:600;margin-top:8px">Contact Us Anytime</p></div>
    <div class="subscribe">Enter Your Email<span>SUBSCRIBE</span></div>
    <div class="rule"></div>
    <p class="copyright">Copyright DelphineCarrow 2021 | All Right Reserver</p>
    <div class="social" aria-label="Social links"><b></b><b></b><b></b><b></b></div>
  </footer>
  <div class="abs footer-flower" role="img" aria-label="Photograph of a small pink gerbera flower"></div>

</div>
</body>
</html>
```